Industrial Company-Pop-Up Banner Design for Demolition and Infrastructure Company

Hi-
We need to create 2 pop-up banners for our company. They will both have the same logo, but different photos. We would like to have the colors white, red, and black and feature a modern design. I have attached some inspiration photos.

Target Market(s)

Trade Show/Job Fair Audience

Industry/Entity Type

construction, industrial

Font styles to use
Sans Serif

Colors
EB3D1F
EC4F4E
F09395
F8D3D4
FCEDEE

Requirements
Must have
• 2 versions, each with different photos but same design. Logo, Red, Black, and White Color Scheme, Modern Design
Nice to have
• Modern Design similar to the inspiration photos

```html
<!DOCTYPE html>
<html lang="en">
<head>
<meta charset="utf-8">
<title>R.K. Harlow Companies – Pop-up Banners</title>
<link rel="stylesheet" href="https://fonts.googleapis.com/css2?family=Anton&family=Great+Vibes&family=Montserrat:wght@700;800&family=Oswald:wght@600&display=swap">
<style>
  :root {
    --red: #ee1c1c;
    --red-deep: #d81414;
    --black: #0b0b0b;
    --black-soft: #1e1e1e;
    --white: #ffffff;
    --backdrop: #e4e4e4;
  }
  html, body {
    margin: 0;
    width: 1200px;
    height: 917px;
    overflow: hidden;
    background: var(--backdrop);
  }
  .stage { position: relative; width: 1200px; height: 917px; }
  .banner {
    position: absolute;
    top: 78px;
    width: 452px;
    height: 738px;
    display: block;
  }
  .banner--one { left: 100px; }
  .banner--two { left: 658px; }
  .brand-name { font-family: "Montserrat", sans-serif; font-weight: 800; fill: var(--white); }
  .headline { font-family: "Anton", sans-serif; fill: var(--red); }
  .headline-script { font-family: "Great Vibes", cursive; fill: var(--white); }
  .since { font-family: "Montserrat", sans-serif; font-weight: 800; fill: var(--white); }
  .emergency-label { font-family: "Oswald", sans-serif; font-weight: 600; fill: var(--red); }
  .phone { font-family: "Montserrat", sans-serif; font-weight: 800; fill: var(--white); }
  .web { font-family: "Montserrat", sans-serif; font-weight: 700; fill: var(--white); }
  .web-accent { fill: var(--red); }
  .red-shape { fill: var(--red); }
  .photo-frame { stroke: var(--white); stroke-width: 9; }
</style>
</head>
<body>
<main class="stage">

  <!-- Banner one -->
  <svg class="banner banner--one" viewBox="0 0 565 922" role="group" aria-label="Pop-up banner, version one">
    <defs>
      <clipPath id="b1-clip"><rect width="565" height="922"/></clipPath>
      <linearGradient id="b1-bg" x1="0" y1="0" x2="0" y2="1">
        <stop offset="0" stop-color="#1b1b1b"/><stop offset="1" stop-color="#050505"/>
      </linearGradient>
      <linearGradient id="b1-p1" x1="0" y1="0" x2="1" y2="1">
        <stop offset="0" stop-color="#9fb0a4"/><stop offset=".45" stop-color="#4f6b3c"/><stop offset="1" stop-color="#2f4a26"/>
      </linearGradient>
      <linearGradient id="b1-p2" x1="0" y1="0" x2="1" y2="1">
        <stop offset="0" stop-color="#5d7a3a"/><stop offset=".5" stop-color="#b9a37a"/><stop offset="1" stop-color="#7a6a4d"/>
      </linearGradient>
      <linearGradient id="b1-p3" x1="0" y1="0" x2="0" y2="1">
        <stop offset="0" stop-color="#7fa6d6"/><stop offset=".45" stop-color="#4d7a3a"/><stop offset="1" stop-color="#c9a77c"/>
      </linearGradient>
      <linearGradient id="b1-p4" x1="0" y1="0" x2="1" y2="1">
        <stop offset="0" stop-color="#d9dde2"/><stop offset=".5" stop-color="#8fa7b8"/><stop offset="1" stop-color="#4b5b55"/>
      </linearGradient>
    </defs>
    <g clip-path="url(#b1-clip)">
      <rect width="565" height="922" fill="url(#b1-bg)"/>

      <g class="brand">
        <rect x="34" y="88" width="34" height="34" class="red-shape"/>
        <text class="brand-name" x="80" y="105" font-size="20">R.K. HARLOW</text>
        <text class="brand-name" x="80" y="128" font-size="20">COMPANIES</text>
      </g>

      <text class="headline" x="256" y="101" font-size="62" textLength="221" lengthAdjust="spacingAndGlyphs">SHAPING</text>
      <text class="headline" x="256" y="168" font-size="62" textLength="268" lengthAdjust="spacingAndGlyphs">AMERICA'S</text>
      <text class="headline-script" x="254" y="228" font-size="54">Skyline</text>
      <rect x="400" y="196" width="126" height="29" class="red-shape"/>
      <text class="since" x="463" y="218" font-size="19" text-anchor="middle">Since 1959</text>

      <polygon class="red-shape" points="0,202 80,282 0,358"/>
      <polygon class="red-shape" points="0,662 90,752 0,838"/>
      <polygon class="red-shape" points="565,288 458,395 565,502"/>
      <polygon class="red-shape" points="565,760 403,922 565,922"/>
      <polygon class="red-shape" points="215,307 245,337 215,367 185,337"/>
      <polygon class="red-shape" points="450,317 480,347 450,377 420,347"/>

      <g role="img" aria-label="Photo: aerial view of power lines crossing green wetlands">
        <polygon class="photo-frame" fill="url(#b1-p1)" points="97,292 317,512 97,732 -123,512"/>
      </g>
      <g role="img" aria-label="Photo: excavator working beside a large pipe on a cleared site">
        <polygon class="photo-frame" fill="url(#b1-p2)" points="345,282 453,390 345,498 237,390"/>
      </g>
      <g role="img" aria-label="Photo: earthmoving equipment grading a wide dirt site">
        <polygon class="photo-frame" fill="url(#b1-p3)" points="447,415 549,517 447,619 345,517"/>
      </g>
      <g role="img" aria-label="Photo: controlled demolition of a power plant with twin striped stacks">
        <polygon class="photo-frame" fill="url(#b1-p4)" points="345,527 578,760 345,993 112,760"/>
      </g>

      <polygon fill="var(--black)" points="0,860 112,748 286,922 0,922"/>
      <text class="emergency-label" x="38" y="850" font-size="13">EMERGENCY SERVICES:</text>
      <text class="phone" x="36" y="880" font-size="26">800-555-0142</text>
      <text class="web" x="33" y="901" font-size="16">www.<tspan class="web-accent">rkharlow</tspan>.com</text>
    </g>
  </svg>

  <!-- Banner two -->
  <svg class="banner banner--two" viewBox="0 0 565 922" role="group" aria-label="Pop-up banner, version two">
    <defs>
      <clipPath id="b2-clip"><rect width="565" height="922"/></clipPath>
      <linearGradient id="b2-bg" x1="0" y1="0" x2="0" y2="1">
        <stop offset="0" stop-color="#1b1b1b"/><stop offset="1" stop-color="#050505"/>
      </linearGradient>
      <linearGradient id="b2-p1" x1="0" y1="0" x2="0" y2="1">
        <stop offset="0" stop-color="#dfe5ea"/><stop offset=".5" stop-color="#c9b25a"/><stop offset=".7" stop-color="#b83a2c"/><stop offset="1" stop-color="#7b7468"/>
      </linearGradient>
      <linearGradient id="b2-p2" x1="0" y1="0" x2="0" y2="1">
        <stop offset="0" stop-color="#a9c6df"/><stop offset=".4" stop-color="#d8b83a"/><stop offset="1" stop-color="#b86e44"/>
      </linearGradient>
      <linearGradient id="b2-p3" x1="0" y1="0" x2="0" y2="1">
        <stop offset="0" stop-color="#c8d8e6"/><stop offset=".4" stop-color="#6b8a4a"/><stop offset="1" stop-color="#a8603e"/>
      </linearGradient>
      <linearGradient id="b2-p4" x1="0" y1="0" x2="1" y2="1">
        <stop offset="0" stop-color="#cfd3d4"/><stop offset=".5" stop-color="#7b756c"/><stop offset="1" stop-color="#4a6d96"/>
      </linearGradient>
    </defs>
    <g clip-path="url(#b2-clip)">
      <rect width="565" height="922" fill="url(#b2-bg)"/>

      <g class="brand">
        <rect x="34" y="88" width="34" height="34" class="red-shape"/>
        <text class="brand-name" x="80" y="105" font-size="20">R.K. HARLOW</text>
        <text class="brand-name" x="80" y="128" font-size="20">COMPANIES</text>
      </g>

      <text class="headline" x="256" y="101" font-size="62" textLength="221" lengthAdjust="spacingAndGlyphs">SHAPING</text>
      <text class="headline" x="256" y="168" font-size="62" textLength="268" lengthAdjust="spacingAndGlyphs">AMERICA'S</text>
      <text class="headline-script" x="254" y="228" font-size="54">Skyline</text>
      <rect x="400" y="196" width="126" height="29" class="red-shape"/>
      <text class="since" x="463" y="218" font-size="19" text-anchor="middle">Since 1959</text>

      <polygon class="red-shape" points="0,202 80,282 0,358"/>
      <polygon class="red-shape" points="0,662 90,752 0,838"/>
      <polygon class="red-shape" points="565,288 458,395 565,502"/>
      <polygon class="red-shape" points="565,760 403,922 565,922"/>
      <polygon class="red-shape" points="215,307 245,337 215,367 185,337"/>
      <polygon class="red-shape" points="450,317 480,347 450,377 420,347"/>

      <g role="img" aria-label="Photo: excavator demolishing an industrial brewery building">
        <polygon class="photo-frame" fill="url(#b2-p1)" points="97,292 317,512 97,732 -123,512"/>
      </g>
      <g role="img" aria-label="Photo: excavator loading a haul truck on a red clay site">
        <polygon class="photo-frame" fill="url(#b2-p2)" points="345,282 453,390 345,498 237,390"/>
      </g>
      <g role="img" aria-label="Photo: excavator clearing a graded red dirt field">
        <polygon class="photo-frame" fill="url(#b2-p3)" points="447,415 549,517 447,619 345,517"/>
      </g>
      <g role="img" aria-label="Photo: high-reach machines tearing down a multi-storey building">
        <polygon class="photo-frame" fill="url(#b2-p4)" points="345,527 578,760 345,993 112,760"/>
      </g>

      <polygon fill="var(--black)" points="0,860 112,748 286,922 0,922"/>
      <text class="emergency-label" x="38" y="850" font-size="13">EMERGENCY SERVICES:</text>
      <text class="phone" x="36" y="880" font-size="26">800-555-0142</text>
      <text class="web" x="33" y="901" font-size="16">www.<tspan class="web-accent">rkharlow</tspan>.com</text>
    </g>
  </svg>

</main>
</body>
</html>
```